Window Graphics

there are a couple things we are trying to rebrand our shop with a new logo, the current Logo I am attaching we want to have something new and refreshing with a hint of fashion with a simple logo that is easy to remember, the name of the company is Marlow Threads Wholesale, our website is marlowthreads.com we also have a retail store that the window graphics needs to be completely redone as pictured. the sign on top will also need to be redone keep in mind we are a wholesale shop so we can to attract customers that are driving easily, the window measurements are 9 windows, window #8 should tell the customers to use the other door because there is no entrance from here
all sizes below are the width of the window
1. 37
2. 30
3. 37
4. 36
5. 30
6. 42
7. 30
8. 30
9. 30

```html
<!DOCTYPE html>
<html lang="en">
<head>
<meta charset="utf-8">
<title>Marlow Threads Wholesale — Window Graphics</title>
<link rel="stylesheet" href="https://fonts.googleapis.com/css2?family=Anton&family=Archivo+Black&family=Bebas+Neue&family=Montserrat:wght@600;800&family=Orbitron:wght@700&display=swap">
<style>
  :root {
    --sheet: #cfcfcf;
    --label: #707070;
    --red: #e30613;
    --white: #ffffff;
    --ink: #0a0a0a;
  }
  * { margin: 0; padding: 0; box-sizing: border-box; }
  html, body { width: 1200px; height: 934px; overflow: hidden; background: var(--sheet); }
  .sheet { position: relative; width: 1200px; height: 934px; }

  .window-number {
    position: absolute; width: 154px; text-align: center;
    font-family: "Orbitron", sans-serif; font-weight: 700; font-size: 30px;
    color: var(--label); line-height: 1;
  }

  .window { position: absolute; width: 154px; height: 312px; overflow: hidden; }
  .window--red { background: var(--red); }
  .window--white { background: var(--white); }

  .photo { position: absolute; }
  .abs { position: absolute; white-space: nowrap; line-height: 1; }

  .url {
    font-family: "Montserrat", sans-serif; font-weight: 600;
    font-size: 6.6px; letter-spacing: 1.6px;
  }
  .col-down { writing-mode: vertical-rl; }
  .col-up { writing-mode: vertical-rl; transform: rotate(180deg); }
  .col-upright { writing-mode: vertical-rl; text-orientation: upright; }
  .stretch { transform-origin: left top; }

  .outline-word {
    font-family: "Orbitron", sans-serif; font-weight: 700; font-size: 40px;
    color: transparent; -webkit-text-stroke: 1.6px var(--white); letter-spacing: 2px;
  }
  .geo-word { font-family: "Montserrat", sans-serif; font-weight: 800; }
  .block-word { font-family: "Archivo Black", sans-serif; }
  .tall-word { font-family: "Bebas Neue", sans-serif; }
  .heavy-word { font-family: "Anton", sans-serif; }
</style>
</head>
<body>
<main class="sheet">

  <!-- Row one -->
  <span class="window-number" style="left:161px;top:81px">1</span>
  <span class="window-number" style="left:342px;top:81px">2</span>
  <span class="window-number" style="left:523px;top:81px">3</span>
  <span class="window-number" style="left:703px;top:81px">4</span>
  <span class="window-number" style="left:884px;top:81px">5</span>

  <!-- 1 Hoodies -->
  <section class="window window--red" style="left:161px;top:120px">
    <div class="photo" role="img" aria-label="Smiling woman in a cropped beige hoodie and blue jeans"
         style="left:42px;top:14px;width:112px;height:298px;background:linear-gradient(180deg,#e6d2b8 0%,#dcc3a4 60%,#6f8fbf 75%,#4f6fa3 100%);border-radius:40px 0 0 0"></div>
    <div class="abs col-down outline-word" style="left:8px;top:8px">HOODIES</div>
  </section>

  <!-- 2 Jackets -->
  <section class="window window--white" style="left:342px;top:120px">
    <div class="abs url" style="left:12px;top:10px;color:var(--ink)">MARLOWTHREADS.COM</div>
    <div class="photo" role="img" aria-label="Man in a glossy black puffer vest and black track pants"
         style="left:12px;top:26px;width:84px;height:284px;background:linear-gradient(180deg,#2a2a2a 0%,#1a1a1a 40%,#e8e8e8 45%,#222 55%,#1b1b1b 100%);border-radius:30px 30px 8px 8px"></div>
    <div class="abs col-upright block-word" style="left:100px;top:10px;font-size:40px;color:var(--ink);line-height:44px">JACKETS</div>
  </section>

  <!-- 3 Harlan -->
  <section class="window window--red" style="left:523px;top:120px">
    <div class="photo" role="img" aria-label="Young man in a mustard crewneck sweatshirt and dark jeans"
         style="left:0;top:16px;width:132px;height:296px;background:linear-gradient(180deg,#c9a07e 0%,#d7a428 25%,#d19a20 75%,#1d2433 85%,#1d2433 100%);border-radius:40px 40px 0 0"></div>
    <div class="abs col-up geo-word" style="left:104px;top:14px;font-size:41px;letter-spacing:3px;color:var(--ink)">HARLAN</div>
    <div class="abs url" style="left:30px;top:300px;color:var(--white)">MARLOWTHREADS.COM</div>
  </section>

  <!-- 4 Polo -->
  <section class="window window--white" style="left:703px;top:120px">
    <div class="abs tall-word stretch" style="left:11px;top:8px;font-size:78px;letter-spacing:3px;color:var(--red);transform:scaleY(1.15)">POLO</div>
    <div class="abs col-up url" style="left:10px;top:88px;color:var(--ink)">MARLOWTHREADS.COM</div>
    <div class="photo" role="img" aria-label="Young man in a charcoal polo shirt and grey pants"
         style="left:26px;top:78px;width:114px;height:234px;background:linear-gradient(180deg,#cfa88c 0%,#4a4b50 22%,#44454a 80%,#cfcfcf 90%,#d6d6d6 100%);border-radius:36px 36px 0 0"></div>
  </section>

  <!-- 5 Tanktop -->
  <section class="window window--red" style="left:884px;top:120px">
    <div class="photo" role="img" aria-label="Man in a royal blue tank top"
         style="left:34px;top:35px;width:120px;height:277px;background:linear-gradient(180deg,#b78666 0%,#b78666 30%,#1f56c4 34%,#1e4fb8 90%,#1a1a1a 100%);border-radius:44px 44px 0 0"></div>
    <div class="abs col-up geo-word" style="left:10px;top:8px;font-size:34px;letter-spacing:1px;color:var(--white)">TANKTOP</div>
    <div class="abs col-up url" style="left:137px;top:10px;color:var(--white)">MARLOWTHREADS.COM</div>
  </section>

  <!-- Row two -->
  <span class="window-number" style="left:255px;top:469px">6</span>
  <span class="window-number" style="left:444px;top:469px">7</span>
  <span class="window-number" style="left:634px;top:469px">8</span>
  <span class="window-number" style="left:823px;top:469px">9</span>

  <!-- 6 Headwear -->
  <section class="window window--white" style="left:255px;top:502px">
    <div class="abs tall-word stretch" style="left:18px;top:14px;font-size:66px;letter-spacing:3px;color:var(--red);transform:scaleY(1.2)">HEAD</div>
    <div class="photo" role="img" aria-label="Woman adjusting a tan cap, wearing a black v-neck tee"
         style="left:0;top:110px;width:154px;height:202px;background:linear-gradient(180deg,#c9a882 0%,#c9a882 15%,#e2b899 28%,#222 50%,#1c1c1c 100%);border-radius:60px 60px 0 0"></div>
    <div class="abs heavy-word stretch" style="left:17px;top:72px;font-size:56px;letter-spacing:0;color:var(--ink);transform:scaleY(1.2)">WEAR</div>
  </section>

  <!-- 7 Joggers -->
  <section class="window window--red" style="left:444px;top:502px">
    <div class="photo" role="img" aria-label="Woman in a mustard hoodie and matching joggers with white sneakers"
         style="left:14px;top:14px;width:86px;height:278px;background:linear-gradient(180deg,#d7b394 0%,#d9b352 18%,#d4ad4c 88%,#f2f2f2 94%,#f2f2f2 100%);border-radius:34px 34px 10px 10px"></div>
    <div class="abs col-down geo-word" style="left:100px;top:10px;font-size:44px;letter-spacing:2px;color:var(--ink)">JOGGERS</div>
    <div class="abs url" style="left:12px;top:295px;color:var(--white)">MARLOWTHREADS.COM</div>
  </section>

  <!-- 8 Use other door / Youth joggers -->
  <section class="window window--white" style="left:634px;top:502px">
    <div class="abs" style="left:0;top:0;width:154px;height:91px;background:var(--red)"></div>
    <div class="abs tall-word" style="left:9px;top:8px;font-size:44px;letter-spacing:-0.5px;color:var(--white)">USE OTHER</div>
    <div class="abs tall-word" style="left:9px;top:46px;font-size:44px;letter-spacing:-0.5px;color:var(--white)">DOOR</div>
    <svg class="abs" style="left:93px;top:55px" width="44" height="26" viewBox="0 0 44 26" aria-hidden="true">
      <g fill="none" stroke="var(--white)" stroke-width="4" stroke-linejoin="miter">
        <polyline points="3,3 13,13 3,23"/>
        <polyline points="16,3 26,13 16,23"/>
        <polyline points="29,3 39,13 29,23"/>
      </g>
    </svg>
    <div class="photo" role="img" aria-label="Young girl in a pale pink tee and red joggers"
         style="left:8px;top:100px;width:86px;height:196px;background:linear-gradient(180deg,#8a5a3b 0%,#e2bfa4 16%,#f6e6ea 28%,#f3dde2 42%,#e0242b 48%,#d9232a 92%,#eeeeee 100%);border-radius:30px 30px 8px 8px"></div>
    <div class="abs col-up geo-word" style="left:74px;top:104px;font-size:44px;letter-spacing:2px;color:var(--red)">YOUTH</div>
    <div class="abs col-down geo-word" style="left:118px;top:104px;font-size:24px;letter-spacing:3px;color:var(--ink)">JOGGERS</div>
  </section>

  <!-- 9 Youth tees -->
  <section class="window window--red" style="left:823px;top:502px">
    <div class="abs col-up geo-word" style="left:8px;top:8px;font-size:18px;letter-spacing:1px;color:var(--white)">YOUTH</div>
    <div class="abs tall-word stretch" style="left:29px;top:4px;font-size:78px;letter-spacing:-1px;color:var(--white);transform:scaleY(1.25)">TEES</div>
    <div class="photo" role="img" aria-label="Curly-haired boy in a sand colored tee and cream pants"
         style="left:18px;top:88px;width:124px;height:224px;background:linear-gradient(180deg,#b8874a 0%,#e1bfa3 20%,#dfcfbd 36%,#d9c8b4 88%,#efe8da 94%,#efe8da 100%);border-radius:44px 44px 0 0"></div>
  </section>

</main>
</body>
</html>
```